Need modern simple design for magazine ad, apartment and condo roofer.

I need a half page magazine ad for a local roofer to publish in an industry magazine. Apartment associations industry. All types of roofs. Shingle and Flat
Need the design to be creative and modern, clean and simple. I do not want a busy design. One that stands out and makes a point quickly.
Logo must be prominent.
DO NOT USE PHOTOS FROM MY WEBSITE PLEASE. Looking for something new.
I work on entire complexes not houses.

Need to make sure our phone number and email address are listed at the bottom. Here is my website www.vorbelan.com
Want to stay away from standard clip arts of tools, homes, apartment buildings.
Half Horizontal 7.25 x 4.75
Ads should be in PDF and JPG format.

Target Market(s)

Apartment or Condo owners looking for large scale roofing projects

Industry/Entity Type

Roofing

Requirements
Must have
• Prominent Logo
Simple Clean Design
Create graphics
Not Busy
Should not have
• Clip Art
No Photos from my website

```html
<!DOCTYPE html>
<html lang="en">
<head>
<meta charset="utf-8">
<title>Crestline Multifamily Roofing – Half Page Ad</title>
<link href="https://fonts.googleapis.com/css2?family=Montserrat:wght@400;500;700;800&display=swap" rel="stylesheet">
<style>
  :root {
    --brand-blue: #1f78c1;
    --ink: #2b2b2b;
    --paper: #ffffff;
    --band: rgba(28, 30, 30, 0.62);
    --water-light: #6f8d86;
    --water-dark: #2f4a44;
    --foliage: #3f5a34;
    --roof: #b9826a;
  }
  * { margin: 0; padding: 0; box-sizing: border-box; }
  html, body {
    width: 1200px; height: 786px; overflow: hidden;
    background: var(--paper);
    font-family: "Montserrat", Arial, sans-serif;
  }
  .ad {
    position: relative; width: 1200px; height: 786px;
    background: var(--paper);
  }
  .hero-scene {
    position: absolute; left: 0; top: 0; width: 1200px; height: 549px;
    background:
      radial-gradient(ellipse 60% 30% at 60% 75%, var(--water-dark) 0%, transparent 70%),
      radial-gradient(ellipse 45% 25% at 85% 20%, rgba(185,130,106,0.45) 0%, transparent 70%),
      radial-gradient(ellipse 40% 25% at 20% 25%, rgba(185,130,106,0.35) 0%, transparent 70%),
      linear-gradient(180deg, #9fb3b0 0%, var(--foliage) 30%, var(--water-light) 48%, var(--water-dark) 72%, #4c5e4d 100%);
  }
  .headline-band {
    position: absolute; left: 0; top: 257px; width: 1200px; height: 107px;
    background: var(--band);
    display: flex; align-items: center; justify-content: center;
  }
  .headline {
    color: #fff; font-weight: 800; font-size: 53px; letter-spacing: 0.2px;
    white-space: nowrap;
  }
  .intro {
    position: absolute; left: 58px; top: 588px; width: 720px;
    color: var(--ink); font-size: 17.4px; line-height: 25px; font-weight: 500;
  }
  .intro .company { color: var(--brand-blue); font-weight: 700; }
  .contact {
    position: absolute; left: 57px; top: 694px;
    color: var(--brand-blue); font-weight: 700; font-size: 37px;
    white-space: nowrap;
  }
  .contact .divider { margin: 0 18px; }
  .brand-mark {
    position: absolute; left: 846px; top: 668px; width: 300px;
    display: flex; align-items: center; gap: 12px;
  }
  .brand-mark .square {
    width: 44px; height: 44px; background: var(--brand-blue); flex: none;
  }
  .brand-mark .name {
    color: var(--brand-blue); font-weight: 700; font-size: 22px; line-height: 26px;
  }
</style>
</head>
<body>
  <main class="ad">
    <div class="hero-scene" role="img" aria-label="Aerial view of a waterfront residential community with villas, condominium blocks, canals, moored boats and tropical greenery"></div>
    <div class="headline-band">
      <h1 class="headline">ADDING VALUE WITH A WIDER VIEW.</h1>
    </div>
    <p class="intro">
      <span class="company">Crestline Multifamily Roofing Inc</span> has been improving and adding value
      to multifamily apartment communities and student housing developments for
      over 30 years now., looking for the perfect solution based on your needs.
    </p>
    <p class="contact">
      <span class="phone">817.555.0148</span><span class="divider">|</span><span class="email">info@vorbelan.com</span>
    </p>
    <div class="brand-mark">
      <span class="square"></span>
      <span class="name">Crestline<br>Multifamily Roofing</span>
    </div>
  </main>
</body>
</html>
```